Tolby Insurance Agency Menu of Insurance Services

We are a 4th generation family business that wants to be able to hand out a "menu" of insurance services we offer. We insure a lot of restaurants so we like being able to give THEM a menu when they give US one. We currently need to update ours because not only is it a little too wordy, but our logo is blurry on the cover. We are looking for a fun but professional design that includes some pictures. Thank you!

Target Market(s)

All ages, but we have a lot of clients that have been with us for 30+ years, so cross-selling to them (50 and 60 year olds) is very important to us.

Industry/Entity Type

Insurance Broker

Font styles to use
Serif

Colors

Designer to choose colors to be used in the design.

Requirements
Must have
• A brief about our family agency as well as insurance services we offer
Nice to have
• If our logo could be edited so that it doesn't look blurry when printed, that would be awesome! We also like pictures that are funny to keep things light because no one is really going to read an "insurance menu" without something unique, like pictures.

```html
<!DOCTYPE html>
<html lang="en">
<head>
<meta charset="utf-8">
<title>Tolby Insurance Agency – Menu of Insurance Services</title>
<link href="https://fonts.googleapis.com/css2?family=Noto+Serif:wght@400;700&display=swap" rel="stylesheet">
<style>
:root{
  --board:#b9babc;
  --paper:#ffffff;
  --cream:#fdeec0;
  --orange:#e8692a;
  --orange-light:#f6a33a;
  --ink:#111111;
  --text:#3a3a3a;
  --social:#3b5a9a;
  --photo-blue:#7d9bb8;
  --photo-green:#6f8f52;
  --photo-dark:#1c2a22;
  --photo-warm:#b79a78;
}
*{box-sizing:border-box;margin:0;padding:0}
html,body{width:1138px;height:1200px;overflow:hidden;background:var(--board)}
body{position:relative;font-family:"Noto Serif",serif;color:var(--text)}
.abs{position:absolute}
.spread{position:absolute;left:42px;width:699px;height:540px;background:var(--paper);overflow:hidden}
.spread--outside{top:39px}
.spread--inside{top:610px}
.panel{position:absolute;top:0;width:233px;height:540px;overflow:hidden}
.panel--fade{background:linear-gradient(to bottom,var(--paper) 45%,var(--cream) 100%)}
.panel--fade-top{background:linear-gradient(to bottom,var(--cream) 0%,var(--paper) 30%)}
.panel--yellow{background:linear-gradient(to bottom,var(--cream),var(--paper) 30%,var(--paper) 60%,var(--cream))}
.band{position:absolute;left:0;right:0;bottom:0;height:7px;background:linear-gradient(to right,var(--orange-light),var(--orange) 12%,var(--ink) 13%,var(--ink) 87%,var(--orange) 88%,var(--orange-light))}
.photo{position:absolute}
.headline{position:absolute;left:0;width:233px;text-align:center;color:var(--orange);font-size:23px;line-height:29px;font-weight:400}
.intro{position:absolute;left:18px;width:197px;text-align:center;font-size:11.3px;line-height:14.5px}
.phone{position:absolute;left:0;width:233px;text-align:center;color:var(--orange);font-size:24px;line-height:26px}
.web{position:absolute;left:0;width:233px;text-align:center;color:var(--text);font-size:12px;line-height:14px}
.vertical{position:absolute;transform:rotate(-90deg);transform-origin:left top;white-space:nowrap;font-size:8.2px;line-height:9.6px;color:var(--text)}
.vertical b{color:var(--orange);font-weight:700}
.social{color:var(--social);font-size:9px;line-height:11px;font-weight:700}
.cover-title{position:absolute;background:var(--ink);color:var(--paper);font-size:28px;line-height:36px;padding:10px 12px;box-shadow:-5px -5px 0 var(--orange-light)}
.year{position:absolute;background:var(--orange);color:var(--paper);font-size:12px;font-weight:700;text-align:center;line-height:16px}
.wordmark{position:absolute;left:0;width:233px;text-align:center;font-size:30px;font-weight:700;color:var(--ink);line-height:34px}
.wordmark span{display:inline-block;width:14px;height:14px;background:var(--ink);margin-right:8px;vertical-align:middle}
.cover-phone{font-size:22px;line-height:24px}
.cover-web{font-size:10px;line-height:12px}
.service{position:absolute;width:233px}
.service .icon{position:absolute;width:38px;height:38px;border-radius:50%;background:var(--orange);border:2px solid var(--paper)}
.service .icon i{position:absolute;left:11px;top:12px;width:12px;height:10px;background:var(--paper);border-radius:2px}
.service h3{position:absolute;color:var(--orange);font-size:12.5px;line-height:15px;font-weight:700;white-space:nowrap}
.service p{position:absolute;font-size:7.5px;line-height:10.5px;color:var(--text)}
</style>
</head>
<body>

<section class="spread spread--outside">
  <div class="panel panel--fade" style="left:0">
    <div class="photo" role="img" aria-label="Photo of a team meeting around an office table with laptops" style="left:11px;top:11px;width:211px;height:163px;background:linear-gradient(160deg,#e9ecef,#c9cfd6 60%,#8a8f96)"></div>
    <h2 class="headline" style="top:186px">WE ARE HERE<br>FOR YOU</h2>
    <p class="intro" style="top:256px">Tired of paying too much for your current insurance? Not sure if you're properly covered?</p>
    <p class="intro" style="top:323px">Check out all of the services Tolby Insurance Agency provides before and after your policy is written! Our 4th generation family-owned business can help you save time and money, while demonstrating A+ service.</p>
    <p class="phone" style="top:468px">847.555.0142</p>
    <p class="web" style="top:497px">tolbyinsurance.com</p>
  </div>

  <div class="panel panel--fade" style="left:233px">
    <div class="photo" role="img" aria-label="Photo of a pink piggy bank with coins and a calculator" style="left:95px;top:206px;width:137px;height:230px;background:radial-gradient(ellipse at 50% 60%,#f6c9c4,#f3e3d0 55%,rgba(255,255,255,0) 75%)"></div>
    <div class="abs" style="left:46px;top:218px;width:34px;height:42px;border-radius:50%;background:var(--orange);color:var(--paper);font-size:6px;line-height:8px;text-align:center;padding-top:12px">Hablamos<br>Español</div>
    <p class="vertical" style="left:22px;top:341px"><b>Other coverages we offer:</b><br>Intellectual Property<br>Wedding<br>Flood<br>Travel<br>Much, much more!</p>
    <p class="vertical" style="left:22px;top:513px"><b>Tolby Insurance Agency, Inc.</b><br>410 Orchard Avenue, Suite 120<br>Lakeview Park, IL 60099<br><br>Phone: 847.555.0142<br>Fax: 847.555.0198<br>tolbyinsurance.com</p>
    <div class="abs" style="left:187px;top:489px;width:22px;height:24px;background:var(--social)"></div>
    <p class="vertical social" style="left:186px;top:480px">"like" us on Friendbook</p>
  </div>

  <div class="panel panel--fade" style="left:466px">
    <div class="photo" role="img" aria-label="Photo of the agency family standing behind an outdoor information table" style="left:0;top:0;width:233px;height:304px;background:linear-gradient(to bottom,#5f7f45,#93b07a 35%,#c69aa8 60%,#8b86c2)"></div>
    <div class="cover-title" style="left:27px;top:198px;width:155px;height:164px">Tolby<br>Insurance<br>Agency,<br>Inc.</div>
    <div class="year" style="left:125px;top:352px;width:49px">1932</div>
    <p class="wordmark" style="top:418px"><span></span>TOLBY</p>
    <p class="phone cover-phone" style="top:487px">847.555.0142</p>
    <p class="web cover-web" style="top:510px">tolbyinsurance.com</p>
  </div>
  <div class="band"></div>
</section>

<section class="spread spread--inside">
  <div class="panel panel--fade-top" style="left:0"></div>
  <div class="panel panel--yellow" style="left:233px"></div>
  <div class="panel" style="left:466px;background:var(--paper)"></div>

  <article class="service" style="left:0;top:0">
    <div class="photo" role="img" aria-label="Photo of a parent and teen driver in a blue car" style="left:11px;top:11px;width:211px;height:141px;background:linear-gradient(to bottom,var(--photo-dark),var(--photo-blue) 55%,#4d6a88)"></div>
    <div class="icon" style="left:15px;top:139px"><i></i></div>
    <h3 style="left:57px;top:160px">Automobile</h3>
    <p style="left:16px;top:182px;width:208px">Auto insurance getting expensive? Any young drivers in the family? We represent several auto and home-owners insurers who will help you "bundle" coverages &amp; maximize good-student and multi-car discounts</p>
  </article>
  <article class="service" style="left:0;top:256px">
    <div class="photo" role="img" aria-label="Photo of a stone-fronted family house with a blue door" style="left:11px;top:11px;width:211px;height:141px;background:linear-gradient(to bottom,#9fc0e0,#b7a58c 40%,var(--photo-green))"></div>
    <div class="icon" style="left:15px;top:142px"><i></i></div>
    <h3 style="left:62px;top:167px">Homeowners/Renters</h3>
    <p style="left:19px;top:189px;width:208px">Do you know if your house or apartment is properly insured? Any students off to college soon? We can show you how a strong homeowners policy will cover you as well as your student's belongings at school, and when you should get a separate policy for them.</p>
  </article>

  <article class="service" style="left:233px;top:0">
    <div class="photo" role="img" aria-label="Photo of a hooded figure in front of green computer code" style="left:12px;top:10px;width:209px;height:143px;background:linear-gradient(135deg,#1f3b25,#0c130e 60%,#2b2b2b)"></div>
    <div class="icon" style="left:13px;top:143px"><i></i></div>
    <h3 style="left:60px;top:164px">Cyber Liability</h3>
    <p style="left:12px;top:188px;width:210px">We can show you how Employment Practices Liability is normally excluded from your business insurance, but can be written separately to cover harassment, wrongful termination, age discrimination, etc.</p>
  </article>
  <article class="service" style="left:233px;top:256px">
    <div class="photo" role="img" aria-label="Photo of a newspaper clipping on health reform lying on banknotes" style="left:12px;top:11px;width:210px;height:141px;background:linear-gradient(135deg,#d8dcd4,#9aa595 50%,#e7e9e3)"></div>
    <div class="icon" style="left:13px;top:143px"><i></i></div>
    <h3 style="left:62px;top:167px">Health</h3>
    <p style="left:11px;top:187px;width:212px">Wrestling with Health Reform changes? We are fully certified to guide you through the best new plans. We offer individual and group health, senior products, and assistance with plan selection.</p>
  </article>

  <article class="service" style="left:466px;top:0">
    <div class="photo" role="img" aria-label="Photo of restaurant staff taking an order from diners" style="left:11px;top:9px;width:209px;height:143px;background:linear-gradient(to bottom,#e8e6e0,#cfc6b6 50%,#3a3a3a)"></div>
    <div class="icon" style="left:15px;top:141px"><i></i></div>
    <h3 style="left:60px;top:160px">Office, Shops and<br>Restaurants</h3>
    <p style="left:11px;top:196px;width:212px">We can quote several different business insurance carriers for you to locate the best possible coverage. For instance, we represent several of the top restaurants in the country on key coverages such as equipment breakdown and business interruption.</p>
  </article>
  <article class="service" style="left:466px;top:256px">
    <div class="photo" role="img" aria-label="Photo of an injured warehouse worker sitting among cardboard boxes" style="left:11px;top:20px;width:209px;height:140px;background:linear-gradient(to bottom,var(--photo-warm),#8c7660 60%,#6e6a66)"></div>
    <div class="icon" style="left:14px;top:153px"><i></i></div>
    <h3 style="left:60px;top:178px">Worker's Compensation</h3>
    <p style="left:12px;top:202px;width:212px">Not sure when to begin a worker's comp plan for your employees? We can tell you when you need it, help minimize premiums and even assist with year-end audits.</p>
  </article>
  <div class="band"></div>
</section>

<section class="panel panel--fade" style="left:841px;top:252px;width:233px;height:538px">
  <div class="photo" role="img" aria-label="Photo of the agency family standing behind an outdoor information table" style="left:0;top:0;width:233px;height:304px;background:linear-gradient(to bottom,#5f7f45,#93b07a 35%,#c69aa8 60%,#8b86c2)"></div>
  <p class="web cover-web" style="top:509px">tolbyinsurance.com</p>
  <div class="band"></div>
</section>
<section class="panel panel--fade" style="left:806px;top:219px;width:233px;height:539px">
  <div class="photo" role="img" aria-label="Photo of the agency family standing behind an outdoor information table" style="left:0;top:0;width:233px;height:304px;background:linear-gradient(to bottom,#5f7f45,#93b07a 35%,#c69aa8 60%,#8b86c2)"></div>
  <div class="cover-title" style="left:27px;top:198px;width:155px;height:164px">Tolby<br>Insurance<br>Agency,<br>Inc.</div>
  <div class="year" style="left:125px;top:351px;width:49px">1932</div>
  <p class="wordmark" style="top:415px"><span></span>TOLBY</p>
  <p class="phone cover-phone" style="top:486px">847.555.0142</p>
  <p class="web cover-web" style="top:510px">tolbyinsurance.com</p>
  <div class="band"></div>
</section>

</body>
</html>
```